Modern Business Card Design Needed for Young Realtor

Information that is going on the card:Marcus Penhall
Broker/Owner
555.013.2967
Marcus@MPenhallHomes.example
www.MPenhallHomes.example

Would also like to include my Instagram Handle somewhere. Probably on the back: the_queencity_realtorMy previous business card is attached, I like that one but would like an updated version and maybe a few design changes

Marcus Penhall
Broker/Owner
555.013.2967
Marcus@MPenhallHomes.example
www.MPenhallHomes.example

• Would also like to include my Instagram Handle somewhere. Probably on the back: the_harborline_agent
• Brantley Osgood or the BO (logo from the previous card.)

```html
<!DOCTYPE html>
<html lang="en">
<head>
<meta charset="utf-8">
<title>Marcus Penhall – Business Card</title>
<link href="https://fonts.googleapis.com/css2?family=Cinzel:wght@500&family=Roboto:wght@400;500;900&display=swap" rel="stylesheet">
<style>
  :root {
    --page: #2b2b2b;
    --card: #1d1d1f;
    --red: #a61e2b;
    --white: #ffffff;
    --grey: #d9d9d9;
    --photo-a: #7d8a6a;
    --photo-b: #5b6654;
  }
  * { box-sizing: border-box; margin: 0; padding: 0; }
  html, body { width: 1200px; height: 895px; overflow: hidden; background: var(--page); }
  .stage { position: relative; width: 1200px; height: 895px; }

  .card { position: absolute; background: var(--card); overflow: hidden; box-shadow: 0 10px 30px rgba(0,0,0,.45); }

  /* Front: brand side */
  .card-front { left: 40px; top: 247px; width: 700px; height: 400px; }
  .brand { position: absolute; left: 0; right: 0; top: 125px; display: flex; justify-content: center; align-items: center; gap: 16px; }
  .brand-mark { width: 22px; height: 22px; background: var(--red); }
  .brand-name { font-family: "Cinzel", serif; font-weight: 500; font-size: 46px; letter-spacing: 7px; color: var(--white); }
  .front-details { position: absolute; left: 0; right: 0; top: 230px; text-align: center; font-family: "Roboto", sans-serif; color: var(--white); font-size: 17px; line-height: 34px; }
  .front-details .row { display: flex; justify-content: center; align-items: center; gap: 10px; }
  .dot { width: 16px; height: 16px; border-radius: 50%; background: var(--red); }

  /* Back: agent side */
  .card-back { left: 780px; top: 97px; width: 390px; height: 700px; }
  .photo { position: absolute; left: 0; top: 0; width: 390px; height: 420px; background: linear-gradient(160deg, var(--photo-a), var(--photo-b) 60%, #6f6f72); }
  .band { position: absolute; left: 0; top: 0; width: 390px; height: 700px; }
  .agent { position: absolute; left: 30px; top: 395px; font-family: "Roboto", sans-serif; color: var(--white); transform: rotate(-4deg); transform-origin: left top; }
  .agent-name { font-weight: 900; font-size: 34px; letter-spacing: 1px; text-transform: uppercase; }
  .agent-title { font-weight: 400; font-size: 17px; letter-spacing: 1px; margin-top: 2px; }

  .contact-icons { position: absolute; left: 0; right: 0; top: 530px; display: flex; justify-content: center; gap: 12px; }
  .contact-icons svg { width: 26px; height: 26px; }
  .contacts { position: absolute; left: 0; right: 0; top: 572px; text-align: center; font-family: "Roboto", sans-serif; font-weight: 500; color: var(--white); font-size: 17px; line-height: 27px; }
  .contacts .accent { color: var(--red); }
  .badges { position: absolute; left: 24px; bottom: 22px; display: flex; gap: 8px; }
  .badge { width: 26px; height: 26px; border: 2px solid var(--white); }
</style>
</head>
<body>
<main class="stage">

  <section class="card card-front" aria-label="Card front">
    <div class="brand">
      <span class="brand-mark"></span>
      <span class="brand-name">MPENHALL HOMES</span>
    </div>
    <div class="front-details">
      <div class="row"><span class="dot"></span><span>the_harborline_agent</span></div>
      <div class="row">
        <svg width="14" height="18" viewBox="0 0 14 18" aria-hidden="true"><path d="M7 0a7 7 0 0 0-7 7c0 5 7 11 7 11s7-6 7-11a7 7 0 0 0-7-7zm0 9.5A2.5 2.5 0 1 1 7 4.5a2.5 2.5 0 0 1 0 5z" fill="var(--red)"/></svg>
        <span>1180 Wexmoor Ave Ste. 300, Rivergate, NC 27000</span>
      </div>
    </div>
  </section>

  <section class="card card-back" aria-label="Card back">
    <div class="photo" role="img" aria-label="Portrait photo of the agent in a grey blazer and white shirt, outdoors with greenery behind"></div>
    <svg class="band" viewBox="0 0 390 700" aria-hidden="true">
      <polygon points="0,395 390,365 390,470 0,500" fill="var(--red)"/>
      <polygon points="0,500 390,470 390,478 0,508" fill="var(--white)"/>
      <polygon points="0,508 390,478 390,700 0,700" fill="var(--card)"/>
    </svg>
    <div class="agent">
      <div class="agent-name">Marcus Penhall</div>
      <div class="agent-title">Broker/Owner</div>
    </div>

    <div class="contact-icons" aria-hidden="true">
      <svg viewBox="0 0 26 26"><circle cx="13" cy="13" r="12" fill="none" stroke="var(--white)" stroke-width="1.5"/><path d="M9 7l3 3-1.5 2c1 2 2.5 3.5 4.5 4.5l2-1.5 3 3-2 2c-5 0-11-6-11-11z" fill="var(--red)"/></svg>
      <svg viewBox="0 0 26 26"><circle cx="13" cy="13" r="12" fill="none" stroke="var(--white)" stroke-width="1.5"/><rect x="7" y="9" width="12" height="9" fill="var(--red)"/><path d="M7 9l6 5 6-5" fill="none" stroke="var(--card)" stroke-width="1.2"/></svg>
      <svg viewBox="0 0 26 26"><circle cx="13" cy="13" r="12" fill="none" stroke="var(--white)" stroke-width="1.5"/><circle cx="13" cy="13" r="6" fill="var(--red)"/><path d="M7 13h12M13 7v12" stroke="var(--card)" stroke-width="1"/></svg>
    </div>
    <div class="contacts">
      <div>555.013.2967</div>
      <div>Marcus@MPenhallHomes.example</div>
      <div>www.<span class="accent">MPenhallHomes</span>.example</div>
    </div>
    <div class="badges" aria-hidden="true">
      <span class="badge"></span>
      <span class="badge"></span>
    </div>
  </section>

</main>
</body>
</html>
```